Fenwick Partners - Client Appreciation Party Invitation and Poster

We need a printable invitation, a version of the same invitation that can be emailed out, and also a Poster of the invitation for our annual client appreciation party.

The location is called: The Larkspur Loft. Here is a link to the location: https://www.thelarkspurloftvenue.com/

We like their font and their little logo that you see when you log onto this page. But we'd love to see creatively what you can come up with.

This party is for our clients who are interior designers and owners in the Hospitality industry. Here are the details which need to be included in the invitation:

Location: The Larkspur Loft - 482 W Tamsin Ave. Chicago IL 60618
Date/Time: Thursday August 23rd - 5:30-9:00pm
RSVP: Please RSVP to: gathering@fenwickpartners.com

Then our Sponsors Logos need to be included on the bottom: I have uploaded those logos here as well as our Logo and a copy of the invitation we did for last year's party so you can see sort of what we've done in the past.

For the poster - we typically do a version of the invitation (see uploaded example of last year's poster) with the sponsor logos and the overall theme of the invitation just a bit simplified by removing the date/time/location info. We need this in a printable format which can be blown up to a 24x30 poster size.

Requirements
Must have
• use 2 to 3 colors only.
• logos of sponsors can be of the same color.

```html
<!DOCTYPE html>
<html lang="en">
<head>
<meta charset="utf-8">
<title>Fenwick Partners – Weekend Warmup Poster</title>
<link rel="stylesheet" href="https://fonts.googleapis.com/css2?family=Montserrat:wght@300;400&family=Permanent+Marker&display=swap">
<style>
  :root {
    --ink: #221f20;
    --red: #c8202f;
    --gold: #f9b03b;
    --white: #ffffff;
  }
  html, body {
    margin: 0;
    padding: 0;
    width: 986px;
    height: 1200px;
    overflow: hidden;
    background: var(--ink);
  }
  .poster {
    position: relative;
    width: 986px;
    height: 1200px;
    background: var(--ink);
    font-family: "Montserrat", sans-serif;
    color: var(--white);
  }
  .ornament {
    position: absolute;
    width: 270px;
    height: 240px;
  }
  .ornament--tl { left: 33px; top: 51px; background: radial-gradient(circle at 12% 12%, rgba(200,32,47,.55), rgba(200,32,47,0) 70%); }
  .ornament--tr { right: 33px; top: 51px; background: radial-gradient(circle at 88% 12%, rgba(200,32,47,.55), rgba(200,32,47,0) 70%); }
  .ornament--bl { left: 33px; top: 928px; background: radial-gradient(circle at 12% 88%, rgba(200,32,47,.55), rgba(200,32,47,0) 70%); }
  .ornament--br { right: 33px; top: 928px; background: radial-gradient(circle at 88% 88%, rgba(200,32,47,.55), rgba(200,32,47,0) 70%); }
  .rule {
    position: absolute;
    background: var(--red);
  }
  .rule--left { left: 55px; top: 290px; width: 3px; height: 650px; }
  .rule--right { left: 928px; top: 290px; width: 3px; height: 650px; }
  .rule--divider { left: 58px; top: 979px; width: 872px; height: 3px; }
  .rule--base { left: 300px; top: 1145px; width: 386px; height: 3px; }

  .host {
    position: absolute;
    top: 100px;
    left: 0;
    width: 986px;
    display: flex;
    justify-content: center;
    align-items: center;
    gap: 14px;
  }
  .host__dot {
    width: 46px;
    height: 46px;
    border: 2px solid var(--white);
    border-radius: 50%;
  }
  .host__name {
    font-weight: 300;
    font-size: 20px;
    letter-spacing: 3px;
  }

  .title {
    position: absolute;
    left: 0;
    width: 986px;
    top: 205px;
    text-align: center;
    font-family: "Permanent Marker", cursive;
    line-height: 1;
  }
  .title__week {
    display: block;
    font-size: 215px;
    color: var(--gold);
    -webkit-text-stroke: 10px var(--red);
    paint-order: stroke fill;
    transform: rotate(-3deg);
    letter-spacing: -6px;
  }
  .title__end {
    position: absolute;
    left: 390px;
    top: 210px;
    font-size: 78px;
    color: var(--red);
    -webkit-text-stroke: 6px var(--gold);
    paint-order: stroke fill;
    transform: rotate(-10deg);
  }
  .title__warmup {
    display: block;
    margin-top: 8px;
    font-size: 138px;
    color: var(--white);
    -webkit-text-stroke: 9px var(--red);
    paint-order: stroke fill;
    letter-spacing: -4px;
  }

  .mask-art {
    position: absolute;
    left: 242px;
    top: 643px;
    width: 530px;
    height: 220px;
    border-radius: 110px;
    background: linear-gradient(90deg, rgba(249,176,59,.75), var(--red) 30%, var(--red) 70%, rgba(249,176,59,.75));
  }

  .tagline {
    position: absolute;
    top: 893px;
    left: 0;
    width: 986px;
    text-align: center;
    font-family: "Permanent Marker", cursive;
    font-size: 40px;
    color: var(--gold);
    letter-spacing: 1px;
  }

  .sponsors {
    position: absolute;
    left: 80px;
    width: 826px;
    display: flex;
    justify-content: center;
    align-items: center;
    gap: 48px;
    font-weight: 400;
    color: var(--white);
  }
  .sponsors--top { top: 1005px; font-size: 25px; }
  .sponsors--bottom { top: 1073px; font-size: 28px; }
  .sponsor--small { font-size: 13px; letter-spacing: 1px; }
</style>
</head>
<body>
<main class="poster">
  <div class="ornament ornament--tl" role="img" aria-label="Red scrollwork corner ornament"></div>
  <div class="ornament ornament--tr" role="img" aria-label="Red scrollwork corner ornament"></div>
  <div class="ornament ornament--bl" role="img" aria-label="Red scrollwork corner ornament"></div>
  <div class="ornament ornament--br" role="img" aria-label="Red scrollwork corner ornament"></div>

  <div class="rule rule--left"></div>
  <div class="rule rule--right"></div>
  <div class="rule rule--divider"></div>
  <div class="rule rule--base"></div>

  <header class="host">
    <span class="host__dot"></span>
    <span class="host__name">FENWICK PARTNERS</span>
  </header>

  <h1 class="title">
    <span class="title__week">WEEK</span>
    <span class="title__end">END</span>
    <span class="title__warmup">WARMUP</span>
  </h1>

  <div class="mask-art" role="img" aria-label="Striped red masquerade mask with gold flame accents"></div>

  <p class="tagline">CLIENT APPRECIATION PARTY</p>

  <div class="sponsors sponsors--top">
    <span class="sponsor">Orlo</span>
    <span class="sponsor">Brantley Hospitality</span>
    <span class="sponsor">Meridell Lighting</span>
    <span class="sponsor sponsor--small">VANTOR-KELL</span>
  </div>
  <div class="sponsors sponsors--bottom">
    <span class="sponsor">Hallmere</span>
    <span class="sponsor">LUNARO</span>
  </div>
</main>
</body>
</html>
```